Real Estate Development Company Web Developer

Hi, I am looking for a website developer to create a website for our new real estate development company. you need to design a website with motion graphics that can be run on any device.
We're looking for sample websites like:
https://brackenholm.ca/ or https://www.tarnwellco.ca/
- The website shall include 6 pages with 1 page hidden.
- The website needs to have 2 versions - English and Chinese
- for your mock-up design, you can use copyright free imagery (we are based in Vancouver, and our projects are townhouses/condos, etc)
Please show examples of professional websites you have done & a mock-up website design for our company. We will shortlist in the next several days and get started straight away. The wording for text content will be detailed in a separate document for each page after we decide the designer.

```html
<!DOCTYPE html>
<html lang="en">
<head>
<meta charset="utf-8">
<title>Norvale Properties Group</title>
<link href="https://fonts.googleapis.com/css2?family=Poppins:wght@300;400;500;600;700&display=swap" rel="stylesheet">
<style>
:root{
  --blue:#1f73c1;
  --ink:#222428;
  --dark:#2f3033;
  --muted:#6c6f75;
  --line:#e6e7ea;
  --grey-bg:#f4f5f7;
  --white:#ffffff;
}
*{box-sizing:border-box;margin:0;padding:0}
html,body{width:1200px;height:3096px;overflow:hidden}
body{font-family:'Poppins',sans-serif;color:var(--ink);background:var(--white);position:relative}
.abs{position:absolute}
.center{left:0;width:1200px;text-align:center}

/* hero */
.hero{position:absolute;left:0;top:0;width:1200px;height:590px;
  background:linear-gradient(180deg,#2a2f36 0%,#4a4f55 45%,#3d3a33 75%,#2a2822 100%)}
.hero::after{content:"";position:absolute;inset:0;background:rgba(10,12,16,.35)}
.hero > *{z-index:1}
.brand{position:absolute;left:130px;top:26px;display:flex;align-items:center;gap:8px;
  font-weight:700;font-size:17px;color:var(--white);letter-spacing:.5px}
.brand-dot{width:14px;height:14px;background:var(--white)}
.nav{position:absolute;right:130px;top:26px;display:flex;align-items:center;gap:18px;
  font-size:8px;font-weight:600;color:var(--white);letter-spacing:.3px}
.nav .active{color:var(--blue);border-bottom:1px solid var(--blue);padding-bottom:3px}
.nav .sep{width:1px;height:10px;background:rgba(255,255,255,.5)}
.btn-join{background:var(--blue);color:var(--white);border-radius:12px;padding:6px 14px;display:flex;gap:5px;align-items:center}
.eyebrow{font-size:9px;letter-spacing:2.2px;font-weight:500}
.hero-eyebrow{top:231px;color:var(--white)}
.hero-title{top:248px;font-size:31px;font-weight:500;color:var(--white)}
.hero-text{top:292px;left:360px;width:480px;font-size:10.5px;line-height:15px;color:#e8e8e8;text-align:center}
.btn-pill{display:inline-flex;align-items:center;justify-content:center;gap:6px;border-radius:16px;
  font-size:8.5px;letter-spacing:1.2px;font-weight:500}
.hero-btn{left:548px;top:341px;width:104px;height:28px;background:var(--white);color:var(--ink)}
.hero-down{left:585px;top:544px;width:28px;height:28px;border-radius:50%;background:rgba(255,255,255,.18);
  display:flex;align-items:center;justify-content:center}

/* about */
.about-photo{left:130px;top:654px;width:784px;height:391px;
  background:linear-gradient(180deg,#b9cde0 0%,#dfe7ee 40%,#6f7f8c 62%,#94a3ae 100%)}
.about-card{left:756px;top:751px;width:314px;height:263px;background:var(--dark);
  border-right:2px solid var(--blue);padding:40px 38px 0}
.about-card .eyebrow{color:var(--blue);font-size:8px;display:flex;align-items:center;gap:6px}
.about-card .eyebrow i{width:14px;height:1px;background:#bbb;display:block}
.about-card h2{color:var(--white);font-size:22px;font-weight:600;line-height:28px;margin-top:12px}
.about-card p{color:#c9cbcf;font-size:9.5px;line-height:15px;margin-top:10px}
.btn-outline{margin-top:14px;height:24px;width:106px;border:1px solid var(--white);color:var(--white);font-size:8px}

/* stats */
.stat{top:1096px;width:200px;text-align:center}
.stat-icon{width:58px;height:58px;border-radius:50%;background:var(--dark);margin:0 auto;
  display:flex;align-items:center;justify-content:center}
.stat-icon.on{background:var(--blue)}
.stat-num{font-size:24px;font-weight:600;margin-top:12px}
.stat-num.on{color:var(--blue)}
.stat-text{font-size:9.5px;line-height:13px;color:var(--muted);margin-top:4px}
.rule{left:0;top:1292px;width:1200px;height:1px;background:var(--line)}

/* section heads */
.kicker{color:var(--blue);display:flex;justify-content:center;align-items:center;gap:10px}
.kicker i{display:block;width:14px;height:1px;background:#ccc}
.sec-title{font-size:21px;font-weight:600;color:var(--ink)}
.sec-text{left:360px;width:480px;text-align:center;font-size:10px;line-height:16px;color:var(--muted)}

/* services */
.service{top:1474px;width:221px;height:352px}
.svc-photo{width:100%;height:100%;background:linear-gradient(160deg,#3a3d41 0%,#1f2226 55%,#6b6e72 100%)}
.svc-photo.warm{background:linear-gradient(160deg,#c79a5f 0%,#4b3a2d 35%,#1f2226 65%,#5e6166 100%)}
.svc-label{position:absolute;left:0;width:100%;top:288px;text-align:center;color:var(--white);font-size:9px;font-weight:600;letter-spacing:.5px}
.svc-badge{position:absolute;left:88px;bottom:-22px;width:44px;height:44px;border-radius:50%;background:var(--white);
  box-shadow:0 2px 6px rgba(0,0,0,.15);display:flex;align-items:center;justify-content:center}
.svc-hover{position:absolute;inset:0;background:rgba(42,43,46,.93);padding:28px 26px;text-align:center;color:var(--white)}
.svc-hover h3{font-size:13px;font-weight:600;line-height:19px}
.svc-hover p{font-size:9.5px;line-height:15px;color:#cfd1d4;margin-top:8px}
.svc-hover .btn-outline{width:88px;margin-top:12px}

/* projects */
.projects-bg{left:0;top:1908px;width:1200px;height:592px;background:var(--grey-bg)}
.filters{top:2091px;display:flex;justify-content:center;gap:12px;font-size:9px;font-weight:600;letter-spacing:.8px;color:var(--ink)}
.filters .sep{color:#bbb;font-weight:400}
.filters .on{color:var(--blue)}
.project{top:2148px;width:222px;height:222px;overflow:hidden}
.proj-photo{width:100%;height:100%}
.project .cap{position:absolute;left:18px;bottom:20px;color:var(--white)}
.cap b{display:block;font-size:11px;font-weight:600}
.cap span{font-size:8.5px}
.project .tint{position:absolute;inset:0;background:rgba(40,70,130,.55)}
.proj-arrow{position:absolute;left:18px;top:22px;width:24px;height:24px;border-radius:50%;background:var(--blue);display:flex;align-items:center;justify-content:center}
.view-all{left:526px;top:2395px;width:142px;height:27px;background:var(--blue);color:var(--white);font-size:8px}

/* support */
.support{left:0;top:2500px;width:1200px;height:270px;
  background:linear-gradient(180deg,#6b7680 0%,#58626a 45%,#4a4a3c 75%,#5a4630 100%)}
.support::after{content:"";position:absolute;inset:0;background:rgba(20,25,30,.45)}
.sup-btn{left:531px;top:2675px;width:138px;height:27px;background:var(--white);color:var(--ink)}

/* footer */
.foot-brand{left:170px;top:2838px;font-weight:700;font-size:17px;color:var(--blue);display:flex;gap:8px;align-items:center}
.foot-brand i{width:14px;height:14px;background:var(--blue);display:block}
.socials{left:197px;top:2886px;display:flex;gap:8px}
.socials span{width:24px;height:24px;border-radius:50%;border:1px solid var(--line);display:block}
.fcol{top:2834px;width:150px}
.fcol h4{font-size:8.5px;font-weight:500;letter-spacing:1px;color:var(--muted)}
.fcol h4::after{content:"";display:block;width:16px;height:1px;background:var(--blue);margin-top:9px}
.fcol ul{list-style:none;margin-top:10px}
.fcol li{font-size:9.5px;line-height:18px;color:var(--muted)}
.fcol .on{color:var(--blue)}
.fcol p{font-size:9.5px;line-height:12px;color:var(--muted);margin-top:8px}
.fcol small{display:block;color:#aaa;font-size:9px}
.email-field{margin-top:10px;width:222px;height:26px;border-radius:13px;background:#f0f1f3;display:flex;align-items:center;
  justify-content:space-between;padding:0 14px;font-size:9px;color:#999}
.foot-rule{left:130px;top:3040px;width:940px;height:1px;background:var(--line)}
.copy{left:130px;top:3060px;font-size:8.5px;color:#aaa}
.legal{right:130px;top:3060px;font-size:8px;letter-spacing:.5px;color:var(--muted);display:flex;gap:26px}
</style>
</head>
<body>

<header class="hero" role="img" aria-label="Evening skyline of downtown towers seen from above">
  <div class="brand"><span class="brand-dot"></span>NORVALE</div>
  <nav class="nav">
    <span class="active">HOME</span><span>ABOUT US</span><span>OUR SERVICES</span><span>PROJECTS</span><span>CONTACT US</span>
    <span class="sep"></span><span>中文</span>
    <span class="btn-join"><svg width="9" height="9" viewBox="0 0 10 10" fill="none" stroke="#fff"><circle cx="5" cy="3" r="2"/><path d="M1 9c0-2 2-3 4-3s4 1 4 3"/></svg>JOIN US</span>
  </nav>
  <div class="abs center eyebrow hero-eyebrow">CREATING OPPORTUNITIES</div>
  <h1 class="abs center hero-title">Lorem Ipsum Is Simply</h1>
  <p class="abs hero-text">Lorem Ipsum is simply dummy text of the printing and typesetting industry. Lorem Ipsum has been the industry's standard dummy text ever since the 1500s</p>
  <span class="abs btn-pill hero-btn">EXPLORE MORE</span>
  <span class="abs hero-down"><svg width="10" height="6" viewBox="0 0 10 6" fill="none" stroke="#fff" stroke-width="1.4"><path d="M1 1l4 4 4-4"/></svg></span>
</header>

<div class="abs about-photo" role="img" aria-label="Harbour waterfront with cruise ship and city towers under a cloudy sky"></div>
<section class="abs about-card">
  <div class="eyebrow">ABOUT <i></i></div>
  <h2>Lorem Ipsum is simply dummy text</h2>
  <p>Lorem Ipsum is simply dummy text of the printing and typesetting industry. Lorem Ipsum has been the industry's standard dummy text ever since the 1500s</p>
  <span class="btn-pill btn-outline">MORE ABOUT US</span>
</section>

<div class="abs stat" style="left:140px">
  <div class="stat-icon"><svg width="24" height="24" viewBox="0 0 24 24" fill="none" stroke="#fff" stroke-width="1.2"><circle cx="12" cy="12" r="9"/><ellipse cx="12" cy="12" rx="4" ry="9"/><path d="M3 12h18M5 7h14M5 17h14"/></svg></div>
  <div class="stat-num">5,000</div>
  <div class="stat-text">Lorem Ipsum is simply dummy text of<br>the printing and typesetting</div>
</div>
<div class="abs stat" style="left:380px">
  <div class="stat-icon on"><svg width="24" height="24" viewBox="0 0 24 24" fill="none" stroke="#fff" stroke-width="1.4"><circle cx="10" cy="10" r="6"/><path d="M14.5 14.5L20 20M7.5 10l2 2 3-4"/></svg></div>
  <div class="stat-num on">4,500</div>
  <div class="stat-text">Lorem Ipsum is simply dummy text of<br>the printing and typesetting</div>
</div>
<div class="abs stat" style="left:620px">
  <div class="stat-icon"><svg width="24" height="24" viewBox="0 0 24 24" fill="none" stroke="#fff" stroke-width="1.2"><circle cx="12" cy="12" r="9"/><circle cx="12" cy="12" r="5"/><path d="M12 9v6M10.5 10.5h3M10.5 13.5h3"/></svg></div>
  <div class="stat-num">€250M</div>
  <div class="stat-text">Lorem Ipsum is simply dummy text of<br>the printing and typesetting</div>
</div>
<div class="abs stat" style="left:860px">
  <div class="stat-icon"><svg width="24" height="24" viewBox="0 0 24 24" fill="none" stroke="#fff" stroke-width="1.2"><rect x="5" y="5" width="14" height="11"/><path d="M3 19h18M9 16v-4l3-3 3 3v4"/></svg></div>
  <div class="stat-num">2017–18</div>
  <div class="stat-text">Lorem Ipsum is simply dummy text of<br>the printing and typesetting</div>
</div>
<div class="abs rule"></div>

<div class="abs center eyebrow kicker" style="top:1358px"><i></i>SERVICES<i></i></div>
<h2 class="abs center sec-title" style="top:1377px">LOREM IPSUM IS SIMPLY</h2>
<p class="abs sec-text" style="top:1412px">Lorem Ipsum is simply dummy text of the printing and typesetting industry. Lorem Ipsum has been the industry's standard dummy text ever since the 1500s</p>

<div class="abs service" style="left:130px">
  <div class="svc-photo warm" role="img" aria-label="Building facade with warm lit windows"></div>
  <div class="svc-label">SERVICE 1</div>
  <div class="svc-badge"><svg width="16" height="16" viewBox="0 0 16 16" fill="none" stroke="#333" stroke-width="1.2"><path d="M3 3l5 2 5-2v6l-5 4-5-4z"/></svg></div>
</div>
<div class="abs service" style="left:370px">
  <div class="svc-photo" role="img" aria-label="Modern concrete balconies"></div>
  <div class="svc-hover">
    <h3>Lorem Ipsum Is Simply Dummy</h3>
    <p>Lorem Ipsum is simply dummy text of the printing and typesetting industry. Lorem Ipsum has been the industry's standard dummy text ever since the 1500s</p>
    <span class="btn-pill btn-outline">LEARN MORE</span>
  </div>
</div>
<div class="abs service" style="left:609px">
  <div class="svc-photo" role="img" aria-label="Angled balconies of a residential tower"></div>
  <div class="svc-label">SERVICE 3</div>
  <div class="svc-badge"><svg width="16" height="16" viewBox="0 0 16 16" fill="none" stroke="#333" stroke-width="1.2"><path d="M2 12l4-4 3 3 5-5M11 6h3v3"/></svg></div>
</div>
<div class="abs service" style="left:849px">
  <div class="svc-photo" role="img" aria-label="Balcony rows of a contemporary building"></div>
  <div class="svc-label">SERVICE 4</div>
  <div class="svc-badge"><svg width="16" height="16" viewBox="0 0 16 16" fill="none" stroke="#333" stroke-width="1.2"><rect x="2" y="2" width="12" height="12"/><path d="M5 5v6M8 5v6M11 5v6"/></svg></div>
</div>

<div class="abs projects-bg"></div>
<div class="abs center eyebrow kicker" style="top:1974px"><i></i>PROJECTS<i></i></div>
<h2 class="abs center sec-title" style="top:1993px">LOREM IPSUM IS SIMPLY</h2>
<p class="abs sec-text" style="top:2028px">Lorem Ipsum is simply dummy text of the printing and typesetting industry. Lorem Ipsum has been the industry's standard dummy text ever since the 1500s</p>
<div class="abs center filters"><span>ALL</span><span class="sep">/</span><span>COMPLETE</span><span class="sep">/</span><span>ONGOING</span><span class="sep">/</span><span class="on">PONTENCIAL</span></div>

<div class="abs project" style="left:136px">
  <div class="proj-photo" role="img" aria-label="Modern villa with pool at dusk" style="background:linear-gradient(180deg,#8d93b8 0%,#a7a3bf 50%,#45485e 100%)"></div>
  <div class="cap"><b>4100 ALDER LANE</b><span>Maple Ridge, BC V2X 1A1, Canada</span></div>
</div>
<div class="abs project" style="left:370px">
  <div class="proj-photo" role="img" aria-label="Contemporary house at twilight" style="background:linear-gradient(180deg,#6c7fa3 0%,#56688d 60%,#3a4765 100%)"></div>
  <div class="tint"></div>
  <span class="proj-arrow"><svg width="8" height="8" viewBox="0 0 8 8" fill="none" stroke="#fff" stroke-width="1.2"><path d="M1 4h6M4 1l3 3-3 3"/></svg></span>
  <div class="cap" style="bottom:26px"><b>4100 ALDER LANE</b><span>Maple Ridge, BC V2X 1A1, Canada</span></div>
</div>
<div class="abs project" style="left:604px">
  <div class="proj-photo" role="img" aria-label="Two storey modern home with lit interior" style="background:linear-gradient(180deg,#7b7fa6 0%,#6b5a63 50%,#3b2f2c 100%)"></div>
  <div class="cap"><b>4100 ALDER LANE</b><span>Maple Ridge, BC V2X 1A1, Canada</span></div>
</div>
<div class="abs project" style="left:838px">
  <div class="proj-photo" role="img" aria-label="Single storey home with garden terrace" style="background:linear-gradient(180deg,#b4bac4 0%,#8c8677 55%,#4e5a44 100%)"></div>
  <div class="cap"><b>4100 ALDER LANE</b><span>Maple Ridge, BC V2X 1A1, Canada</span></div>
</div>
<span class="abs btn-pill view-all"><svg width="9" height="9" viewBox="0 0 10 10" fill="none" stroke="#fff"><rect x="1" y="1" width="6" height="6"/><rect x="3" y="3" width="6" height="6"/></svg>VIEW ALL PROJECTS</span>

<section class="abs support" role="img" aria-label="Suspension bridge and city skyline over autumn forest"></section>
<div class="abs center eyebrow kicker" style="top:2565px;color:#fff;z-index:1"><i></i>SUPPORT<i></i></div>
<h2 class="abs center" style="top:2582px;font-size:21px;font-weight:500;color:#fff;z-index:1">GET IN TOUCH</h2>
<p class="abs sec-text" style="top:2619px;color:#eee;z-index:1">Lorem Ipsum is simply dummy text of the printing and typesetting industry. Lorem Ipsum has been the industry's standard dummy text ever since the 1500s</p>
<span class="abs btn-pill sup-btn" style="z-index:1"><svg width="9" height="9" viewBox="0 0 10 10" fill="none" stroke="#333"><circle cx="5" cy="3" r="2"/><path d="M1 9c0-2 2-3 4-3s4 1 4 3"/></svg>CREATE ACCOUNT</span>

<footer>
  <div class="abs foot-brand"><i></i>NORVALE</div>
  <div class="abs socials"><span></span><span></span><span></span></div>
  <div class="abs fcol" style="left:369px">
    <h4>LINKS</h4>
    <ul><li>Home</li><li>About Us</li><li>Our Services</li><li>Projects</li><li>Contact Us</li></ul>
  </div>
  <div class="abs fcol" style="left:529px">
    <h4>SERVICES</h4>
    <p>Lorem Ipsum is simply</p>
    <p class="on">Dummy text of the printing Typesetting industry</p>
    <p>Lorem Ipsum has been the industry</p>
    <p>Standard dummy text ever since the 1500s</p>
  </div>
  <div class="abs fcol" style="left:689px">
    <h4>CONTACT</h4>
    <p><small>Address:</small>0123 Street, City, State, 10000</p>
    <p><small>Phone:</small>+012 345 6789</p>
    <p><small>Email:</small>info@norvale.ca</p>
  </div>
  <div class="abs fcol" style="left:849px;width:222px">
    <h4>NEWSLETTER</h4>
    <p style="color:#999">Subscribe to our emailing list. orem Ipsum is simply dummy text of the printing and typesetting industry.</p>
    <div class="email-field">Your Email Address<svg width="11" height="8" viewBox="0 0 11 8" fill="none" stroke="#888"><rect x=".5" y=".5" width="10" height="7"/><path d="M.5 .5l5 4 5-4"/></svg></div>
  </div>
  <div class="abs foot-rule"></div>
  <div class="abs copy">© Copyright 2022 Norvale Properties Group LTD. All Rights Reserved</div>
  <div class="abs legal"><span>PRIVACY POLICY</span><span>TERMS &amp; CONDITIONS</span></div>
</footer>

</body>
</html>
```